Business Card for Flight Instructor/Commercial Pilot

I need a business card for myself as a Flight Instructor. I'm a certificated flight instructor at a local flight school in St Paul, MN and want to have a business card that I can give out both to prospective students and also to prospective employers in commercial/business aviation. The business card should have a few elements to it (my name, my position, and my TCB certifications:
Dorian Pellew, MBA
Flight Instructor
CFI, CFII, AGI, IGI
Then lastly, I'd like it to include my phone number for calls or texts, my email address, and my Workvine url. I'll provide all of these at a later point.

If we can include some kind of aviation graphic, that's great, but I don't currently have a logo and I don't necessarily need one, so don't feel like a logo is required here, it's not. I'm but I'm open to whatever you might put together. But I honestly don't need a logo, just good design with a simple graphic element to draw a little interest.
I'd also like to add a short tag line. A few ideas I have are:
- Fly Smart. Stay Humble. Never Stop Learning.
- Train smart. Fly safe. Have fun.
- Master the craft. Enjoy the flight.

For the back side, I'm open to ideas on what to put there. maybe the tagline could go there, or a QR code for my Workvine page, or maybe something else.

Target audience is both prospective students who are interested in learning to fly (or adding more ratings) and commercial aviation companies that could be potential employer for me in commercial aviation. Trying to portray a sense of professionalism, trust, and high level of competency.

The business card doesn’t have to be standard (rectangular with square corners) and I’m open to suggestions for based on the design.
Lastly, I just don't want the design created by AI.
Let me know if you need any further info. Thanks!

```html
<!DOCTYPE html>
<html lang="en">
<head>
<meta charset="utf-8">
<title>Dorian Pellew – Flight Instructor Business Card</title>
<link rel="stylesheet" href="https://fonts.googleapis.com/css2?family=Arimo:wght@400;700&family=Ubuntu:wght@400&family=Montserrat:wght@600&display=swap">
<style>
  :root {
    --navy: #00579c;
    --mid-blue: #4f86c6;
    --sky: #a4c2f8;
    --paper: #ffffff;
    --ghost: #f1f1f0;
    --ink: #2b2b2b;
    --link-blue: #1f5fa0;
    --backdrop: #e9ecf2;
  }
  html, body {
    margin: 0;
    width: 1200px;
    height: 1200px;
    overflow: hidden;
    background: var(--backdrop);
  }
  .sheet {
    position: relative;
    width: 1200px;
    height: 1200px;
  }
  .card {
    position: absolute;
    left: 160px;
    width: 880px;
    height: 512px;
    background: var(--paper);
    box-shadow: 0 6px 18px rgba(30, 50, 90, 0.18);
  }
  .card--front { top: 64px; }
  .card--back { top: 624px; }
  .card svg { display: block; width: 880px; height: 512px; }
  .name {
    font-family: "Arimo", Arial, sans-serif;
    font-weight: 700;
    font-size: 35px;
    fill: var(--ink);
    text-decoration: underline;
  }
  .role {
    font-family: "Arimo", Arial, sans-serif;
    font-size: 24px;
    fill: var(--ink);
  }
  .certs {
    font-family: "Arimo", Arial, sans-serif;
    font-weight: 700;
    font-size: 18px;
    fill: var(--ink);
  }
  .contact {
    font-family: "Ubuntu", sans-serif;
    font-size: 21px;
    fill: var(--link-blue);
  }
  .tagline {
    font-family: "Montserrat", sans-serif;
    font-weight: 600;
    font-size: 34px;
    fill: var(--paper);
  }
</style>
</head>
<body>
<main class="sheet">

  <!-- Front of card -->
  <section class="card card--front" aria-label="Card front">
    <svg viewBox="0 0 880 512" xmlns="http://www.w3.org/2000/svg">
      <!-- header band -->
      <rect class="header-band" x="0" y="0" width="880" height="140" fill="var(--sky)"/>
      <path class="header-swoosh-mid" d="M0,0 H100 Q320,110 640,140 H0 Z" fill="var(--mid-blue)"/>
      <path class="header-swoosh-white" d="M155,0 H215 Q330,95 640,140 Q340,120 155,0 Z" fill="var(--paper)"/>
      <path class="header-swoosh-white" d="M60,0 H112 Q300,105 600,140 Q260,110 60,0 Z" fill="var(--paper)" opacity="0.9"/>
      <path class="header-swoosh-navy" d="M0,65 Q260,135 560,140 H0 Z" fill="var(--navy)"/>
      <rect class="header-rule" x="0" y="138" width="880" height="4" fill="var(--navy)"/>
      <!-- airplane graphic -->
      <rect class="airplane-art" x="600" y="22" width="230" height="92" rx="40" fill="var(--paper)" opacity="0.85"
            role="img" aria-label="White airliner silhouette climbing with contrail"/>

      <!-- faint yoke watermark -->
      <rect class="yoke-watermark" x="110" y="150" width="660" height="362" rx="90" fill="var(--ghost)"
            role="img" aria-label="Faint control yoke silhouette"/>

      <!-- bottom accents -->
      <path d="M105,512 Q150,500 230,508 L230,512 Z" fill="var(--navy)"/>
      <path d="M665,508 Q720,500 775,512 L665,512 Z" fill="var(--navy)"/>

      <!-- identity -->
      <text class="name" x="440" y="253" text-anchor="middle">Dorian Pellew, MBA</text>
      <text class="role" x="440" y="290" text-anchor="middle">Flight Instructor</text>
      <text class="certs" x="440" y="325" text-anchor="middle">[ CFI, CFII, AGI, IGI ]</text>

      <!-- contact -->
      <g class="contact-list">
        <circle cx="350" cy="396" r="8" fill="var(--link-blue)"/>
        <path d="M346,392 q1,6 8,8 l1.5,-2 -2.5,-1.5 -1.2,1 q-2,-1 -3,-3 l1,-1.2 -1.5,-2.5 Z" fill="var(--paper)"/>
        <text class="contact" x="372" y="403">012-555-0147</text>

        <rect x="342" y="418" width="16" height="11" fill="var(--link-blue)"/>
        <path d="M342,418 L350,425 L358,418" fill="none" stroke="var(--paper)" stroke-width="1.5"/>
        <text class="contact" x="372" y="430">dorian_pellew@</text>

        <path d="M350,444 a6,6 0 0 1 6,6 c0,5 -6,11 -6,11 c0,0 -6,-6 -6,-11 a6,6 0 0 1 6,-6 Z" fill="var(--link-blue)"/>
        <circle cx="350" cy="450" r="2.2" fill="var(--paper)"/>
        <text class="contact" x="372" y="458">to be location</text>
      </g>
    </svg>
  </section>

  <!-- Back of card -->
  <section class="card card--back" aria-label="Card back">
    <svg viewBox="0 0 880 512" xmlns="http://www.w3.org/2000/svg">
      <!-- top stripe -->
      <rect class="top-stripe" x="0" y="0" width="880" height="20" fill="var(--navy)"/>
      <path d="M610,20 L628,0 H735 L717,20 Z" fill="var(--mid-blue)"/>
      <path d="M735,20 L753,0 H880 V20 Z" fill="var(--sky)"/>

      <!-- yoke graphic -->
      <rect class="yoke-art" x="85" y="110" width="290" height="165" rx="40" fill="var(--sky)"
            role="img" aria-label="Control yoke graphic"/>

      <!-- airplane graphic -->
      <rect class="airplane-art" x="550" y="128" width="220" height="115" rx="50" fill="var(--mid-blue)"
            role="img" aria-label="Airliner silhouette climbing with contrail"/>

      <!-- swooshes -->
      <path class="swoosh-mid" d="M0,318 Q280,385 560,250 Q290,405 0,345 Z" fill="var(--mid-blue)"/>
      <path class="swoosh-navy" d="M0,372 Q200,392 410,335 Q280,410 185,432 H880 V512 H0 Z" fill="var(--navy)"/>
      <rect class="tagline-band" x="0" y="430" width="880" height="82" fill="var(--navy)"/>

      <text class="tagline" x="440" y="484" text-anchor="middle">TRAIN SMART • FLY SAFE • HAVE FUN</text>
    </svg>
  </section>

</main>
</body>
</html>
```